Property Developer Business card design

we need a business card design + printing for a new Property developer company based in melbourne.
We are a group of investors investing in a property developer business. We have more projects involved in residential property as opposed to commercial property but we are involved in both market. we also provide consulting services with overseas investors willing to invest in the australian property market.
Updates
I have uploaded the logo. I'm not very convince with the colors of my logo... any suggestion please?.
Thanks guys!
Target Market(s)
property investors or person willing to purchase investment property
Industry/Entity Type
Residential
Contact Information for Business Card
Harbourne Capital Australia Pty Ltd
Look and feel
Each slider illustrates characteristics of the customer's brand and the style your logo design should communicate.

```html
<!DOCTYPE html>
<html lang="en">
<head>
<meta charset="utf-8">
<title>Harbourne Capital Australia – Business Card</title>
<link href="https://fonts.googleapis.com/css2?family=Open+Sans:wght@400;600;700&display=swap" rel="stylesheet">
<style>
  :root {
    --page-bg: #e9ebee;
    --card-white: #ffffff;
    --brand-red: #8c1d22;
    --brand-red-dark: #6f1418;
    --brand-blue: #2f5a86;
    --logo-blue: #1f86c9;
    --name-blue: #2a6fae;
    --accent-red: #d3262e;
    --text-white: #ffffff;
  }
  * { margin: 0; padding: 0; box-sizing: border-box; }
  html, body { width: 1200px; height: 841px; overflow: hidden; }
  body {
    background: var(--page-bg);
    font-family: "Open Sans", Arial, sans-serif;
    position: relative;
  }
  .card {
    position: absolute;
    top: 272px;
    width: 520px;
    height: 297px;
    border-radius: 22px;
    overflow: hidden;
    box-shadow: 0 6px 18px rgba(0,0,0,0.18);
  }
  .card-front { left: 53px; background: var(--card-white); }
  .card-back  { left: 627px; background: var(--brand-blue); }

  .front-wave { position: absolute; inset: 0; }

  .brand-name {
    position: absolute;
    font-weight: 700;
    letter-spacing: 0.2px;
    display: flex;
    align-items: center;
    gap: 10px;
  }
  .brand-mark { width: 16px; height: 16px; border-radius: 50%; }
  .card-front .brand-name {
    left: 34px; top: 52px;
    font-size: 26px; color: var(--logo-blue);
  }
  .card-front .brand-mark { background: var(--accent-red); }

  .holder { position: absolute; right: 30px; top: 46px; text-align: right; }
  .holder-name { font-size: 22px; font-weight: 700; color: var(--name-blue); line-height: 1.1; }
  .holder-title { font-size: 12px; font-weight: 600; color: var(--accent-red); }

  .contact {
    position: absolute; right: 28px; bottom: 20px;
    color: var(--text-white); text-align: right;
    font-size: 10.5px; line-height: 15px;
  }
  .company { font-weight: 700; font-size: 11px; margin-bottom: 2px; }
  .contact-row { display: flex; justify-content: flex-end; align-items: center; gap: 8px; }
  .contact-row svg { width: 11px; height: 11px; fill: none; stroke: var(--text-white); stroke-width: 1.4; }
  .icon-slot { width: 11px; }

  .card-back .brand-name {
    left: 0; right: 0; top: 108px; justify-content: center;
    font-size: 30px; color: var(--text-white);
  }
  .card-back .brand-mark { background: var(--text-white); }
  .web-address {
    position: absolute; left: 0; right: 0; top: 190px;
    text-align: center; color: var(--text-white);
    font-size: 17px; font-weight: 600;
  }
</style>
</head>
<body>

<section class="card card-front">
  <svg class="front-wave" viewBox="0 0 520 297" preserveAspectRatio="none" aria-hidden="true">
    <path d="M0,132 C150,130 280,175 520,138 L520,297 L0,297 Z" fill="var(--brand-red)"/>
    <path d="M0,122 C150,120 280,165 520,128" fill="none" stroke="var(--brand-red)" stroke-width="3"/>
    <path d="M0,140 C160,140 285,184 520,148" fill="none" stroke="#ffffff" stroke-width="2" opacity="0.85"/>
    <path d="M0,152 C170,154 290,196 520,158" fill="none" stroke="var(--brand-red-dark)" stroke-width="5" opacity="0.5"/>
  </svg>

  <div class="brand-name"><span class="brand-mark"></span>Harbourne Capital</div>

  <div class="holder">
    <div class="holder-name">Daniel Reyes</div>
    <div class="holder-title">Managing Director</div>
  </div>

  <div class="contact">
    <div class="company">Harbourne Capital Australia Pty Ltd</div>
    <div class="contact-row"><span>14 Wattlebird Lane</span><span class="icon-slot"></span></div>
    <div class="contact-row"><span>Tarneit VIC 3029</span><span class="icon-slot"></span></div>
    <div class="contact-row"><span>0412 555 018</span>
      <svg viewBox="0 0 12 12"><rect x="3" y="1" width="6" height="10" rx="1"/></svg></div>
    <div class="contact-row"><span>+61 3 9000 1234</span>
      <svg viewBox="0 0 12 12"><path d="M3,1 L5,3 L4,5 Q5,7 7,8 L9,7 L11,9 L9,11 Q3,10 1,3 Z"/></svg></div>
    <div class="contact-row"><span>daniel.reyes@harbournecapital.com.au</span>
      <svg viewBox="0 0 12 12"><rect x="1" y="2.5" width="10" height="7"/><path d="M1,2.5 L6,7 L11,2.5"/></svg></div>
    <div class="contact-row"><span>www.harbournecapital.com.au</span>
      <svg viewBox="0 0 12 12"><circle cx="6" cy="6" r="5"/><path d="M1,6 H11 M6,1 Q3,6 6,11 Q9,6 6,1"/></svg></div>
  </div>
</section>

<section class="card card-back">
  <div class="brand-name"><span class="brand-mark"></span>Harbourne Capital</div>
  <div class="web-address">www.harbournecapital.com.au</div>
</section>

</body>
</html>
```